Velvet Orchard Club Members Site

To design a website template that is mobile and desktop friendly for the high net worth members, inner circle club for the rich.
Design of the website must be of luxury feel, a club for the rich.
This website offers redemption of luxury items such as travel packages, and many other items.

Below are the page templates required:

MEMBER SITE

- Login Page
- Dashboard Page (Consists of the member’s redemption points summary, expiry dates)
- Categories Page (The main categories of luxury to redeem)
- Product Page (The actual product details to redeem, showing price, description, title, remarks)
- Redemption Cart (Like a shopping cart which temporary stores the selected items for redemption)
- Checkout Page (Like shopping cart checkout to confirm redemption, fill in address, contact number, name)
- Redemption History (Show a list of items redeemed, with the redemption points used, date)
- Redemption Product Page (Show the redeem product’s details like price, description, title, remarks, date redeemed, points used)
- Inbox (Messaging towards customer service/support)
- Write Message Page
- Read Message Page
- Change Password Page
- My Profile Page

ADMIN SITE

- Login Page
- Dashboard Page (Consists of the whole system redemption points summary in the whole club)
- Redemption Page (To Approve or Cancel Redemptions, or message member to ask more about the redemption)
- Administrator List (List the admins in the system)
- Change Password Page
- Inbox (Messaging towards customer)
- Write Message Page
- Read Message Page
- My Profile Page
- Product Management -> Product List Page, Add/Remove/Edit Product Page
- Category Management -> Category List Page, Add/Remove/Edit Category Page

Note:
All colours should be easily changeable under one css file.
You are feel to use colour tones that reflect high society, rich inner circle club.
The website must be mobile friendly.

Reason: Logo of website uploaded in project brief, pls use the colours tone from the logo. Thanks.

Target Market(s)

High Networth Individuals

Industry/Entity Type

Club

Coding

Coded - Design and coding required

Number of Pages Required

5+ page

Font styles to use
Serif
Sans Serif
Decorative
Script

Requirements
Must have
• It must be desktop and mobile friendly
• All colours should be easily changeable under one css file.

```html
<!DOCTYPE html>
<html lang="en">
<head>
<meta charset="utf-8">
<title>Velvet Orchard Club – Dashboard</title>
<link href="https://fonts.googleapis.com/css2?family=Roboto:wght@300;400;500&family=Roboto+Condensed:wght@400&display=swap" rel="stylesheet">
<style>
:root{
  --teal:#1e94b4;
  --teal-dark:#127897;
  --mint:#7cc7b1;
  --aqua:#2bb3c0;
  --sidebar:#34343e;
  --sidebar-dark:#2a2a32;
  --sidebar-line:#3e3e48;
  --page:#f2f2f2;
  --card:#ffffff;
  --text:#333;
  --muted:#666;
  --heading:#3a3a3a;
  --star:#f0a818;
  --price:#e08b1c;
  --green:#2aa52a;
  --red:#e04545;
  --purple:#7a3bb0;
  --footer:#3a3a44;
}
*{box-sizing:border-box;margin:0;padding:0}
html,body{width:1161px;height:1200px;overflow:hidden}
body{position:relative;background:var(--page);font-family:Roboto,Arial,sans-serif;color:var(--text)}
.abs{position:absolute}
/* sidebar */
.brand{left:0;top:0;width:260px;height:192px;background:#fff;display:flex;align-items:center;justify-content:center;gap:10px}
.brand-mark{width:18px;height:18px;background:var(--teal)}
.brand-name{font-size:19px;font-weight:500;color:var(--heading);letter-spacing:1px}
.sidebar{left:0;top:192px;width:260px;height:1008px;background:var(--sidebar)}
.profile{height:222px;background:var(--sidebar-dark);text-align:center;color:#fff}
.avatar{width:96px;height:96px;border-radius:50%;border:4px solid #fff;background:linear-gradient(#c9c4bd,#6a6a72);margin:42px auto 10px}
.profile-name{font-size:20px;font-weight:300}
.profile-role{font-size:13px;font-style:italic;color:#ccc}
.nav{list-style:none}
.nav li{height:53px;display:flex;align-items:center;border-bottom:1px solid var(--sidebar-line);color:#fff;font-size:15px}
.nav .ic{width:66px;height:100%;display:flex;align-items:center;justify-content:center;background:var(--sidebar-dark)}
.nav .lbl{flex:1;padding-left:13px}
.nav .chev{width:30px;font-size:16px}
.nav li.active{background:var(--teal)}
.nav li.active .ic{background:var(--teal)}
/* top */
.topbar{left:260px;top:0;width:901px;height:85px;background:#fff}
.search{left:721px;top:27px;width:218px;height:28px;border:1px solid #ddd;font-size:12px;color:#aaa;padding:7px 15px}
.round{top:29px;width:28px;height:28px;border-radius:50%;border:1px solid #ddd}
.badge{top:23px;width:13px;height:13px;border-radius:50%;color:#fff;font-size:9px;text-align:center;line-height:13px}
.menu{left:1101px;top:25px;width:32px;height:32px;border:1px solid #e5e5e5}
.titlebar{left:260px;top:85px;width:901px;height:65px;background:#ececec}
.page-title{left:280px;top:106px;font-size:20px;color:var(--teal);letter-spacing:.5px}
.seg{top:105px;height:26px;border:1px solid #ccc;background:#fff;font-size:12px;color:#555;display:flex;align-items:center;justify-content:center}
.date{top:105px;height:26px;border:1px solid #ccc;background:#fff;font-size:12px;color:#555;padding:6px 12px}
/* tiles */
.tile{top:190px;width:200px;height:148px;color:#fff;text-align:center}
.tile .circle{width:68px;height:68px;border-radius:50%;border:1.5px solid #fff;margin:23px auto 0;display:flex;align-items:center;justify-content:center;position:relative}
.tile .count{position:absolute;right:-12px;top:-10px;width:28px;height:28px;border-radius:50%;background:#fff;font-size:14px;line-height:28px}
.tile .name{margin-top:18px;font-size:16px}
h2{position:absolute;font-size:19px;font-weight:400;letter-spacing:1.5px;color:var(--heading)}
.card{background:var(--card);border:1px solid #e2e2e2}
.act{position:absolute;left:20px;width:470px}
.act .thumb{position:absolute;left:0;top:0;width:61px;height:57px}
.act .t{position:absolute;left:75px;top:2px;font-size:15px}
.act .stars{position:absolute;left:340px;top:4px;color:var(--star);font-size:11px;letter-spacing:1px}
.act .price{position:absolute;right:0;top:2px;color:var(--price);font-size:15px}
.act p{position:absolute;left:75px;top:24px;width:380px;font-size:11.5px;line-height:17px;color:var(--muted)}
.field{position:absolute;left:22px;width:253px;height:36px;border:1px solid #ddd;background:#f7f7f7;font-size:11px;color:#555;padding:11px 10px}
.btn{position:absolute;background:var(--teal);color:#fff;text-align:center}
.checks{position:absolute;left:22px;top:192px;list-style:none;font-size:11px;color:#444}
.checks li{height:21px;display:flex;gap:14px}
.checks li:before{content:"✔";color:var(--purple)}
.notif{position:absolute;left:0;width:261px;height:44px;border-bottom:1px solid #e5e5e5;display:flex;align-items:center;font-size:12px;color:#444}
.notif .st{width:30px;height:100%;border-right:1px solid #e5e5e5;display:flex;align-items:center;justify-content:center}
.notif .st span{width:10px;height:10px;border-radius:50%;color:#fff;font-size:7px;line-height:10px;text-align:center}
.notif .tx{flex:1;padding-left:8px}
.notif .tg{width:53px;height:19px;color:#fff;font-size:11.5px;line-height:19px;text-align:center;margin-right:18px}
.footer{left:260px;top:1093px;width:901px;height:107px;background:var(--footer);color:#fff;text-align:center}
.social{display:flex;gap:5px;justify-content:center;margin-top:10px}
.social span{width:23px;height:23px;border-radius:50%;border:1.5px solid #fff}
</style>
</head>
<body>
<div class="abs brand"><span class="brand-mark"></span><span class="brand-name">VELVET ORCHARD CLUB</span></div>

<aside class="abs sidebar">
  <div class="profile">
    <div class="avatar" role="img" aria-label="Member profile photo"></div>
    <div class="profile-name">Adrian Vale</div>
    <div class="profile-role">Administrator</div>
  </div>
  <ul class="nav">
    <li class="active"><span class="ic"><svg width="18" height="16"><path d="M9 1L1 8h2v7h4v-4h4v4h4V8h2z" fill="#fff"/></svg></span><span class="lbl">Dashboard</span><span class="chev">›</span></li>
    <li><span class="ic"><svg width="20" height="18"><circle cx="7" cy="10" r="5" fill="none" stroke="#fff" stroke-width="3"/><circle cx="15" cy="5" r="3" fill="none" stroke="#fff" stroke-width="2"/></svg></span><span class="lbl">Categories</span><span class="chev">›</span></li>
    <li><span class="ic"><svg width="22" height="18"><rect x="6" y="1" width="9" height="7" fill="#fff"/><rect x="1" y="9" width="9" height="7" fill="#fff"/><rect x="12" y="9" width="9" height="7" fill="#fff"/></svg></span><span class="lbl">Product</span><span class="chev">›</span></li>
    <li><span class="ic"><svg width="20" height="18"><path d="M1 2h3l2 9h10l2-7H6" fill="none" stroke="#fff" stroke-width="2.5"/><circle cx="8" cy="15" r="2" fill="#fff"/><circle cx="15" cy="15" r="2" fill="#fff"/></svg></span><span class="lbl">Redemption Cart</span><span class="chev">›</span></li>
    <li><span class="ic"><svg width="20" height="18"><rect x="2" y="8" width="11" height="9" fill="#fff"/><path d="M10 8V5a3.5 3.5 0 017 0v2" fill="none" stroke="#fff" stroke-width="2.5"/></svg></span><span class="lbl">Checkout</span><span class="chev">›</span></li>
    <li><span class="ic"><svg width="16" height="20"><path d="M8 1a6 6 0 00-6 6c0 5 6 12 6 12s6-7 6-12a6 6 0 00-6-6z" fill="#fff"/><circle cx="8" cy="7" r="2.2" fill="#2a2a32"/></svg></span><span class="lbl">Redemption History</span><span class="chev">›</span></li>
    <li><span class="ic"><svg width="20" height="20"><circle cx="10" cy="10" r="7" fill="none" stroke="#fff" stroke-width="3"/><circle cx="10" cy="10" r="3" fill="none" stroke="#fff" stroke-width="2"/></svg></span><span class="lbl">Redemption Product</span><span class="chev">›</span></li>
    <li><span class="ic"><svg width="20" height="16"><rect x="1" y="1" width="18" height="14" fill="none" stroke="#fff" stroke-width="2"/><path d="M1 2l9 7 9-7" fill="none" stroke="#fff" stroke-width="2"/></svg></span><span class="lbl">Inbox</span><span class="chev">›</span></li>
    <li><span class="ic"><svg width="22" height="16"><rect x="1" y="1" width="20" height="14" fill="none" stroke="#fff" stroke-width="2"/><rect x="4" y="4" width="6" height="5" fill="#fff"/><path d="M12 5h6M12 8h6M4 12h14" stroke="#fff" stroke-width="1.5"/></svg></span><span class="lbl">Read Message</span><span class="chev">›</span></li>
    <li><span class="ic"><svg width="20" height="20"><circle cx="7" cy="7" r="5" fill="none" stroke="#fff" stroke-width="3"/><path d="M10 10l8 8M15 15l-2 2" stroke="#fff" stroke-width="3"/></svg></span><span class="lbl">Change Password</span><span class="chev">›</span></li>
    <li><span class="ic"><svg width="16" height="18"><circle cx="8" cy="5" r="4" fill="#fff"/><path d="M1 18v-3a7 5 0 0114 0v3z" fill="#fff"/></svg></span><span class="lbl">My Profile</span><span class="chev">›</span></li>
  </ul>
</aside>

<header class="abs topbar"></header>
<div class="abs search">Search...</div>
<div class="abs round" style="left:971px"></div><div class="abs badge" style="left:972px;background:var(--green)">2</div>
<div class="abs round" style="left:1014px"></div><div class="abs badge" style="left:1015px;background:#e0571c">3</div>
<div class="abs round" style="left:1057px"></div>
<div class="abs menu"><svg width="30" height="30"><path d="M10 11h10M10 15h10M10 19h10" stroke="#333" stroke-width="2"/></svg></div>

<div class="abs titlebar"></div>
<div class="abs page-title">VELVET ORCHARD.</div>
<div class="abs seg" style="left:712px;width:55px;background:#ececec">Day</div>
<div class="abs seg" style="left:766px;width:54px">Week</div>
<div class="abs seg" style="left:819px;width:45px">Month</div>
<div class="abs date" style="left:891px;width:112px">12-08-2014 <span style="float:right">▦</span></div>
<div class="abs" style="left:1004px;top:112px;font-size:12px">to</div>
<div class="abs date" style="left:1022px;width:110px">12-08-2014 <span style="float:right">▦</span></div>

<div class="abs tile" style="left:293px;background:var(--teal)"><div class="circle"><svg width="30" height="24"><rect x="1" y="6" width="28" height="17" rx="2" fill="#fff"/><rect x="10" y="1" width="10" height="6" fill="none" stroke="#fff" stroke-width="2"/></svg><span class="count" style="color:var(--purple)">4</span></div><div class="name">TOURS</div></div>
<div class="abs tile" style="left:505px;background:var(--mint)"><div class="circle"><svg width="22" height="28"><rect x="1" y="1" width="20" height="26" fill="none" stroke="#fff" stroke-width="2"/><path d="M6 6h3M13 6h3M6 11h3M13 11h3M6 16h3M13 16h3" stroke="#fff" stroke-width="2"/></svg><span class="count" style="color:var(--price)">12</span></div><div class="name">HOTELS</div></div>
<div class="abs tile" style="left:718px;background:var(--aqua)"><div class="circle"><svg width="26" height="26"><path d="M24 2L2 12l9 3 3 9z" fill="#fff"/></svg><span class="count" style="color:var(--green)">8</span></div><div class="name">PACKAGES</div></div>
<div class="abs tile" style="left:932px;background:var(--teal-dark)"><div class="circle"><svg width="18" height="26"><path d="M9 1a8 8 0 00-8 8c0 6 8 16 8 16s8-10 8-16a8 8 0 00-8-8z" fill="#fff"/><circle cx="9" cy="9" r="3" fill="var(--teal-dark)"/></svg><span class="count" style="color:var(--teal)">12</span></div><div class="name">MANAGE LOCATION</div></div>

<h2 style="left:292px;top:378px">RECENT ACTIVITY</h2>
<h2 style="left:830px;top:378px">NEW BOOKINGS</h2>

<section class="abs card" style="left:293px;top:415px;width:512px;height:294px">
  <div class="act" style="top:34px"><div class="thumb" role="img" aria-label="Guests at a party" style="background:linear-gradient(135deg,#c0302a,#3a1a14)"></div><span class="t">Travel &amp; earn rewards!</span><span class="stars">★★★☆☆</span><span class="price">$20.00</span><p>Lorem ipsum dolor sit amet, consectetur adipiscing elit, sed do eiusmod ut labore et dolore magna aliqua. Ut enim ad minim veniam,</p></div>
  <div class="act" style="top:118px"><div class="thumb" role="img" aria-label="Guests on a lawn" style="background:linear-gradient(#a8c0d8,#5f8a3a)"></div><span class="t">Travel &amp; earn rewards!</span><span class="stars">★★★☆☆</span><span class="price">$20.00</span><p>Lorem ipsum dolor sit amet, consectetur adipiscing elit, sed do eiusmod ut labore et dolore magna aliqua. Ut enim ad minim veniam,</p></div>
  <div class="act" style="top:208px"><div class="thumb" role="img" aria-label="Friends celebrating" style="background:linear-gradient(135deg,#b8282a,#e8a070)"></div><span class="t">Travel &amp; earn rewards!</span><span class="stars">★★★☆☆</span><span class="price">$20.00</span><p>Lorem ipsum dolor sit amet, consectetur adipiscing elit, sed do eiusmod ut labore et dolore magna aliqua. Ut enim ad minim veniam,</p></div>
</section>

<section class="abs card" style="left:831px;top:415px;width:302px;height:294px">
  <div class="field" style="top:30px;width:253px">Search travel</div>
  <div class="field" style="top:77px">packages <span style="float:right">▾</span></div>
  <div class="btn" style="left:22px;top:130px;width:253px;height:37px;line-height:37px;font-size:13px">NEW BOOKINGS</div>
  <ul class="checks">
    <li>Duis aute irure dolor in reprehenderit in</li>
    <li>Lorem ipsum dolor sit amet, consectetur</li>
    <li>Nemo enim ipsam voluptatem quia voluptas</li>
    <li>Neque porro quisquam est, qui</li>
  </ul>
</section>

<h2 style="left:292px;top:748px">LOCATION OF CUSTOMERS</h2>
<h2 style="left:580px;top:748px">NOTIFICATION</h2>
<h2 style="left:871px;top:748px">ADVERTISEMENTS</h2>

<section class="abs card" style="left:292px;top:786px;width:263px;height:267px">
  <div role="img" aria-label="Street map showing customer location" style="height:175px;background:linear-gradient(120deg,#9fc6ee 0%,#9fc6ee 30%,#ece8e0 45%,#ece8e0 100%)"></div>
  <svg class="abs" style="left:20px;top:198px" width="12" height="18"><path d="M6 1a5 5 0 00-5 5c0 4 5 11 5 11s5-7 5-11a5 5 0 00-5-5z" fill="#ccc"/></svg>
  <div class="abs" style="left:39px;top:196px;font-size:9px;color:#555;line-height:13px">Velvet Orchard<br><span style="font-size:7.5px;color:#888">14 Harrow Lane<br>Westbrook, RI 02811<br>United States</span></div>
  <div class="btn" style="left:157px;top:218px;width:87px;height:27px;line-height:27px;font-size:8px;background:var(--aqua);letter-spacing:1px">SHARE</div>
</section>

<section class="abs card" style="left:580px;top:786px;width:263px;height:267px">
  <div class="notif" style="top:0"><span class="st"><span style="background:var(--green)">✔</span></span><span class="tx">Travel &amp; earn rewards!</span><span class="tg" style="background:#8cc4e8">Today</span></div>
  <div class="notif" style="top:44px"><span class="st"><span style="background:var(--red)">✕</span></span><span class="tx" style="color:#999">Manage Hotels Itel</span><span class="tg" style="background:var(--teal)">5.00 PM</span></div>
  <div class="notif" style="top:88px"><span class="st"><span style="background:var(--green)">✔</span></span><span class="tx">Advanced Segmentation</span><span class="tg" style="background:var(--mint)">12 Aug</span></div>
  <div class="notif" style="top:132px"><span class="st"><span style="background:var(--green)">✔</span></span><span class="tx">Custom Reporting</span><span class="tg" style="background:#8cc4e8">12 Aug</span></div>
  <div class="notif" style="top:176px"><span class="st"><span style="background:var(--red)">✕</span></span><span class="tx" style="color:#999">Tag campaigns</span><span class="tg" style="background:var(--teal)">22 Aug</span></div>
  <div class="notif" style="top:220px;border-bottom:0"><span class="st"><span style="background:var(--green)">✔</span></span><span class="tx">Travel &amp; earn rewards!</span><span class="tg" style="background:var(--teal)">Today</span></div>
</section>

<section class="abs" style="left:871px;top:787px;width:262px;height:265px;overflow:hidden;background:var(--teal)">
  <div role="img" aria-label="Backpack on a lakeside pier with mountains" class="abs" style="left:0;top:100px;width:262px;height:165px;background:linear-gradient(#c8d4e0 0%,#7c8ea4 35%,#d8c49a 60%,#e89a3c 100%)"></div>
  <svg class="abs" style="left:0;top:80px" width="262" height="60"><path d="M0 0H262V32Q131 80 0 30Z" fill="var(--teal)"/></svg>
  <div class="abs" style="left:0;top:12px;width:262px;text-align:center;color:#fff;font-family:'Roboto Condensed',sans-serif">
    <div style="font-size:19px">Promotions</div>
    <div style="font-size:15px;line-height:22px;margin-top:6px">Sierra Crown Palace Rail<br>Train Journey&nbsp; From<br>Seville (5 Nights / 6 Days)</div>
  </div>
</section>

<footer class="abs footer">
  <div style="margin-top:34px;font-size:11px">©2016&nbsp; VELVET ORCHARD., ALL RIGHTS RESERVED.</div>
  <div class="social"><span></span><span></span><span></span><span></span><span></span></div>
</footer>
</body>
</html>
```